Love pets? Create a veterinary business card that aligns with our new revamped website.

Greetings! We are a five-doctor veterinary hospital that seeks your expertise in designing a new business card that harmonizes with our recently revitalized website: www.tqrn.net. The card should feature our logo, the five doctors, operating hours, contact information, and communicate our purpose and personality.

Contact Information for Business Card

TBA

```html
<!DOCTYPE html>
<html lang="en">
<head>
<meta charset="utf-8">
<title>Maple Hollow Veterinary Hospital – Business Card</title>
<link href="https://fonts.googleapis.com/css2?family=Dancing+Script:wght@500&family=Open+Sans:wght@400;600;700&display=swap" rel="stylesheet">
<style>
  :root {
    --backdrop: #a7a7a7;
    --card: #ece9e4;
    --green: #4a8a3f;
    --brown: #6b4a18;
    --gold: #d8913a;
    --rule: #dcae6e;
  }
  * { margin: 0; padding: 0; box-sizing: border-box; }
  html, body { width: 1200px; height: 1000px; overflow: hidden; }
  body { background: var(--backdrop); position: relative; font-family: "Open Sans", sans-serif; }

  .card {
    position: absolute; left: 293px; width: 613px; height: 352px;
    background: var(--card); border-radius: 24px; overflow: hidden;
  }
  .card-front { top: 113px; }
  .card-back { top: 510px; }

  /* Front lockup */
  .front-brand {
    position: absolute; top: 18px; left: 0; right: 0;
    display: flex; justify-content: center; align-items: center; gap: 8px;
  }
  .brand-dot { width: 40px; height: 40px; border-radius: 50%; background: var(--green); }
  .brand-text { display: flex; flex-direction: column; align-items: flex-start; }
  .brand-name {
    font-family: "Dancing Script", cursive; font-weight: 500;
    color: var(--green); font-size: 29px; line-height: 30px;
  }
  .brand-sub {
    font-weight: 600; color: var(--brown); font-size: 10px; line-height: 12px;
    letter-spacing: 0.2px; margin-left: 6px;
  }

  .divider-v { position: absolute; left: 308px; top: 97px; width: 1.5px; height: 163px; background: var(--rule); }
  .divider-h { position: absolute; left: 8px; right: 10px; top: 277px; height: 1.5px; background: var(--rule); }

  .doctor { position: absolute; width: 300px; text-align: center; }
  .doctor-name {
    font-family: "Dancing Script", cursive; font-weight: 500;
    color: var(--green); font-size: 40px; line-height: 44px;
  }
  .doctor-title { font-weight: 700; color: var(--brown); font-size: 17px; line-height: 20px; margin-top: 5px; }
  .col-left { left: 21px; }
  .col-right { left: 308px; }
  .row-1 { top: 108px; }
  .row-2 { top: 186px; }

  .info { position: absolute; top: 292px; width: 300px; text-align: center; color: var(--green); font-size: 17px; line-height: 22px; }
  .info b { font-weight: 700; }
  .info-hours { left: 18px; }
  .info-contact { left: 305px; font-weight: 700; }

  /* Back */
  .back-curve { position: absolute; inset: 0; }
  .back-dot {
    position: absolute; left: 261px; top: 50px;
    width: 90px; height: 90px; border-radius: 50%; background: var(--green);
  }
  .back-name {
    position: absolute; left: 0; right: 0; top: 172px;
    font-family: "Dancing Script", cursive; font-weight: 500; color: var(--green);
    font-size: 52px; line-height: 60px; text-align: center;
  }
  .back-sub {
    position: absolute; left: 0; right: 0; top: 236px;
    font-weight: 600; color: var(--brown); font-size: 19px; line-height: 24px;
    text-align: center; letter-spacing: 0.3px;
  }
</style>
</head>
<body>

<section class="card card-front">
  <div class="front-brand">
    <span class="brand-dot"></span>
    <div class="brand-text">
      <span class="brand-name">Maple Hollow</span>
      <span class="brand-sub">VETERINARY HOSPITAL</span>
    </div>
  </div>

  <div class="divider-v"></div>

  <div class="doctor col-left row-1"><div class="doctor-name">Paul Hartwell</div><div class="doctor-title">DVM</div></div>
  <div class="doctor col-left row-2"><div class="doctor-name">Nora Tillet</div><div class="doctor-title">DVM</div></div>
  <div class="doctor col-right row-1"><div class="doctor-name">Grace Lindor</div><div class="doctor-title">DVM</div></div>
  <div class="doctor col-right row-2"><div class="doctor-name">Marian Okafor</div><div class="doctor-title">DVM</div></div>

  <div class="divider-h"></div>

  <div class="info info-hours">
    <div><b>Mon-Fri:</b> 7am-6pm</div>
    <div><b>Sat:</b> 8am-12pm</div>
  </div>
  <div class="info info-contact">
    <div>(555) 214-0198</div>
    <div>www.tqrn.net</div>
  </div>
</section>

<section class="card card-back">
  <svg class="back-curve" width="613" height="352" viewBox="0 0 613 352" aria-hidden="true">
    <path d="M0 235 Q306 390 613 235 L613 352 L0 352 Z" fill="var(--green)"/>
    <path d="M0 225 Q306 380 613 225" fill="none" stroke="var(--gold)" stroke-width="3"/>
  </svg>
  <span class="back-dot"></span>
  <div class="back-name">Maple Hollow</div>
  <div class="back-sub">VETERINARY HOSPITAL</div>
</section>

</body>
</html>
```